i would like a business card to leave with customers and potential customers for electrical work and for the supply and install of reverse cycle airconditioning in the domestic and commercial market.
I own my own business and im a sole trader. I have an a'class electrical lisence and also a refrigeration lisence so i am
able to offer complete installations in airconditioning by a fully qualified and lisenced tradesman.
im looking for something that comes across as unique and professional.
i had the coluor black and some gold in mind but open to any coluors.
something like Beacon Electrical & Refrigeration
or Beacon Air.
i will use this design on a business card to advertise through summer to help generate installs through the busy season.

Target Market(s)

Mainly domestic house holds through summer who are in need of airconditioning and reliable information to acomadate thier cooling and heating requirements

Industry/Entity Type

Electrical

Requirements
Must have
• Business name- Beacon
My name- Peter Wollaston
My mobile no- 0457 819 302
My email- prwollaston@tarvel.com.au
Installation & Decomissioning of aiconditioning split systems
LIC NO: KTR 407516
Nice to have
• Beacon Electrical & Refrigeration

```html
<!DOCTYPE html>
<html lang="en">
<head>
<meta charset="utf-8">
<title>Beacon Electrical &amp; Refrigeration – Business Card</title>
<link rel="stylesheet" href="https://fonts.googleapis.com/css2?family=Raleway:wght@300;400&display=swap">
<style>
  :root {
    --page: #ffffff;
    --card: #ffffff;
    --card-edge: #c9c9c9;
    --ink: #2b2b2b;
    --ink-soft: #3a3a3a;
    --band: #8a8a8a;
    --band-text: #ffffff;
    --accent-blue: #1b9ad6;
    --accent-green: #8dbb3c;
  }
  * { margin: 0; padding: 0; box-sizing: border-box; }
  html, body {
    width: 1200px; height: 850px; overflow: hidden;
    background: var(--page);
    font-family: "Raleway", Arial, sans-serif;
    color: var(--ink);
  }
  .canvas { position: relative; width: 1200px; height: 850px; }

  .card {
    position: absolute; left: 329px; width: 568px; height: 327px;
    background: var(--card);
    border: 1.5px solid var(--card-edge);
    border-radius: 7px;
  }
  .card--front { top: 79px; }
  .card--back  { top: 448px; }

  /* brand lockup: square + name */
  .brand { position: absolute; display: flex; flex-direction: column; align-items: center; }
  .brand__square { background: var(--accent-blue); }
  .brand__name {
    font-weight: 400; color: var(--ink); text-align: center; line-height: 1.1;
    letter-spacing: 0.5px;
  }
  .card--front .brand { left: 0; right: 0; top: 44px; }
  .card--front .brand__square { width: 96px; height: 118px; }
  .card--front .brand__name { font-size: 30px; margin-top: 18px; }

  .card--back .brand { left: 330px; width: 210px; top: 66px; }
  .card--back .brand__square { width: 82px; height: 100px; }
  .card--back .brand__name { font-size: 22px; margin-top: 14px; }

  .badge {
    position: absolute; left: 217px; top: 275px;
    width: 34px; height: 36px; background: var(--accent-green);
  }

  /* back details */
  .name-band {
    position: absolute; left: 0; top: 53px; width: 271px; height: 28px;
    background: var(--band); color: var(--band-text);
    font-size: 20px; font-weight: 400; letter-spacing: 0.6px;
    padding-left: 59px; line-height: 28px;
  }
  .services {
    position: absolute; left: 59px; top: 95px;
    font-size: 14.5px; font-weight: 400; line-height: 19px; color: var(--ink-soft);
  }
  .contact { position: absolute; left: 26px; top: 154px; list-style: none; }
  .contact__item {
    display: flex; align-items: center; height: 24px; margin-bottom: 0;
    font-size: 14.5px; color: var(--ink-soft);
  }
  .contact__icon { width: 24px; height: 18px; margin-right: 9px; }
  .licence {
    position: absolute; left: 59px; top: 223px;
    font-size: 12px; color: var(--ink-soft); letter-spacing: 0.3px;
  }
</style>
</head>
<body>
<main class="canvas">

  <section class="card card--front" aria-label="Card front">
    <div class="brand">
      <div class="brand__square"></div>
      <p class="brand__name">Beacon Electrical<br>&amp; Refrigeration</p>
    </div>
    <div class="badge" role="img" aria-label="Authorised badge"></div>
  </section>

  <section class="card card--back" aria-label="Card back">
    <h1 class="name-band">Peter Wollaston</h1>
    <p class="services">Installation &amp; Decomissioning<br>of aiconditioning split systems</p>
    <ul class="contact">
      <li class="contact__item">
        <svg class="contact__icon" viewBox="0 0 24 18" aria-hidden="true">
          <path d="M2 7 C2 2 22 2 22 7 L18 8 L17 5 C14 4 10 4 7 5 L6 8 Z" fill="#1b9ad6"/>
          <path d="M6 9 L18 9 L21 16 L3 16 Z" fill="#1b9ad6"/>
          <circle cx="12" cy="12.5" r="2.3" fill="#fff"/>
        </svg>
        0457 819 302
      </li>
      <li class="contact__item">
        <svg class="contact__icon" viewBox="0 0 24 18" aria-hidden="true">
          <rect x="3" y="3" width="18" height="12" fill="none" stroke="#1b9ad6" stroke-width="1.2"/>
          <path d="M3 3 L12 10 L21 3 M3 15 L10 8.5 M21 15 L14 8.5" fill="none" stroke="#1b9ad6" stroke-width="1.2"/>
        </svg>
        prwollaston@tarvel.com.au
      </li>
    </ul>
    <p class="licence">LIC NO: KTR 407516</p>
    <div class="brand">
      <div class="brand__square"></div>
      <p class="brand__name">Beacon Electrical<br>&amp; Refrigeration</p>
    </div>
  </section>

</main>
</body>
</html>
```